Tidewell Vitality Autumn Kickoff Quest advertisement design

We need an advertisement for a health, fitness and wellbeing company promoting a new service. The Autumn Kickoff Quest is a 10 week challenge where people choose from 2 program streams - either 1. Fat Loss or 2. Build Lean Muscle. Access to 40 group functional fitness sessions a week, access to exclusive discounts from Brisk Pantry Co. (BPC), discounts on personal training, a targeted gym program, full gym access for the duration of the Challenge and access to Exercise Physiologists and a Sports Dietitian. This is an Tidewell Vitality service co-branded with Brisk Pantry Co.. The final design should be in line with the style guide, be motivating and communicate a point of difference in the fitness industry.

Target Market(s)

men and women ages 30-50yrs, interested in improving their health and lifestyle

Industry/Entity Type

Fitness

Font styles to use
Other font styles liked:
• see style guide

Colors
000000
5c5c5c
9d9d9d
33b8a4
00a990

Requirements
Must have
• professional and exclusive look and feel, motivating tone
Nice to have
• clean design, not too overcrowding, use key pieces of information only and try to stay within the style guide for colour scheme (what is indicated below is the closest pick to our style guide but colour codes are within)
Should not have
• My project should not have any images that cheapen the challenge to look more like a general gym or body sculpting boot camp

```html
<!DOCTYPE html>
<html lang="en">
<head>
<meta charset="utf-8">
<title>Autumn Kickoff Quest</title>
<link rel="stylesheet" href="https://fonts.googleapis.com/css2?family=Open+Sans:wght@300;400;600&display=swap">
<style>
  :root {
    --ink: #000000;
    --charcoal: #1b1c1d;
    --slate: #5c5c5c;
    --mist: #9d9d9d;
    --teal: #33b8a4;
    --teal-deep: #00a990;
    --white: #ffffff;
  }
  * { margin: 0; padding: 0; box-sizing: border-box; }
  html, body { width: 849px; height: 1200px; overflow: hidden; background: var(--ink); }
  .poster {
    position: relative;
    width: 849px;
    height: 1200px;
    overflow: hidden;
    font-family: "Open Sans", sans-serif;
    color: var(--white);
  }
  .backdrop {
    position: absolute;
    inset: 0;
    background:
      radial-gradient(ellipse at 30% 28%, #3a3d3f 0%, rgba(40,42,44,0.6) 35%, rgba(0,0,0,0) 70%),
      radial-gradient(ellipse at 80% 60%, #2a2c2d 0%, rgba(0,0,0,0) 60%),
      linear-gradient(180deg, #1e2021 0%, #111213 55%, #060606 100%);
  }
  .content { position: absolute; left: 70px; right: 70px; top: 0; }
  .title {
    position: absolute;
    top: 78px;
    left: 0;
    width: 640px;
    font-weight: 300;
    font-size: 62px;
    line-height: 72px;
    color: var(--teal);
  }
  .streams-intro {
    position: absolute;
    top: 246px;
    left: 0;
    font-weight: 300;
    font-size: 31px;
    color: var(--white);
  }
  .streams {
    position: absolute;
    top: 300px;
    left: 0;
    list-style: none;
  }
  .streams li {
    display: flex;
    align-items: center;
    gap: 14px;
    font-weight: 400;
    font-size: 28px;
    line-height: 38px;
    color: var(--teal);
  }
  .streams svg { width: 24px; height: 24px; }
  .benefits {
    position: absolute;
    top: 395px;
    left: 0;
    list-style: none;
  }
  .benefits li {
    display: flex;
    align-items: center;
    gap: 14px;
    font-size: 18px;
    line-height: 26px;
    color: var(--white);
  }
  .benefits li::before {
    content: "";
    width: 9px;
    height: 9px;
    background: var(--teal);
    flex: none;
  }
  .brand-host {
    position: absolute;
    top: 668px;
    left: 70px;
    font-weight: 300;
    font-size: 44px;
    letter-spacing: 1px;
    color: var(--white);
  }
  .brand-partner {
    position: absolute;
    top: 645px;
    left: 600px;
    display: flex;
    align-items: center;
    gap: 14px;
  }
  .brand-partner .mark {
    width: 40px;
    height: 40px;
    background: var(--slate);
    flex: none;
  }
  .brand-partner .name {
    font-weight: 300;
    font-size: 22px;
    line-height: 28px;
    color: var(--white);
    width: 140px;
  }
  .divider {
    position: absolute;
    top: 792px;
    left: 70px;
    width: 710px;
    height: 2px;
    background: var(--teal);
  }
  .venture {
    position: absolute;
    top: 804px;
    left: 0;
    width: 849px;
    text-align: center;
    font-size: 16px;
    color: var(--teal);
  }
  .copyright {
    position: absolute;
    top: 832px;
    left: 0;
    width: 849px;
    text-align: center;
    font-size: 11px;
    color: var(--mist);
  }
</style>
</head>
<body>
<main class="poster">
  <div class="backdrop" role="img" aria-label="Dark grey textured grunge background"></div>

  <section class="content">
    <h1 class="title">The Autumn Kickoff Quest</h1>
    <p class="streams-intro">2 program streams to choose from:</p>
    <ul class="streams">
      <li>
        <svg viewBox="0 0 24 24" aria-hidden="true"><path d="M3 10v4M6 7v10M6 12h12M18 7v10M21 10v4" stroke="#33b8a4" stroke-width="2.4" fill="none" stroke-linecap="round"/></svg>
        Fat Loss or
      </li>
      <li>
        <svg viewBox="0 0 24 24" aria-hidden="true"><path d="M3 10v4M6 7v10M6 12h12M18 7v10M21 10v4" stroke="#33b8a4" stroke-width="2.4" fill="none" stroke-linecap="round"/></svg>
        Build Lean Muscle.
      </li>
    </ul>
    <ul class="benefits">
      <li>Access to 40 group functional fitness sessions a week</li>
      <li>Access to exclusive discounts from Brisk Pantry Co. (BPC)</li>
      <li>Discounts on personal training</li>
      <li>A targeted gym program</li>
      <li>Full gym access for the duration of the Challenge</li>
      <li>Access to Exercise Physiologists and a Sports Dietitian</li>
    </ul>
  </section>

  <div class="brand-host">Tidewell Vitality</div>
  <div class="brand-partner">
    <span class="mark"></span>
    <span class="name">Brisk Pantry Co.</span>
  </div>

  <div class="divider"></div>
  <p class="venture">A Joint venture of Tidewell Vitality service and Brisk Pantry Co.</p>
  <p class="copyright">©2015 Tidewell Vitality service. All Rights Reserved</p>
</main>
</body>
</html>
```